psd/html for a e wallet payment website designed

hi
i am in need of a psd / html for a whole website designed
the site is a e wallet /payment system i can i will provide a link to what type of style i am looking for but i can not stress this enough i do not want anyone replicating the website i am just providing the links to show you what kind of function and the content that is involved also, i have a srs with detailed pages you can read and refer to if need be
thanks of viewing
Vantoleaf.com
Brisklune.com
marblequivercoin.com
Qrdelivane.com

```html
<!DOCTYPE html>
<html lang="en">
<head>
<meta charset="utf-8">
<title>Payvinta – Simple Payment Network</title>
<link href="https://fonts.googleapis.com/css2?family=Open+Sans:wght@400;600;700&display=swap" rel="stylesheet">
<style>
:root{
  --orange:#f26522;
  --ink:#333;
  --muted:#8a8a8a;
  --line:#dcdcdc;
  --hero:#f1f1f1;
  --band:#ececec;
  --white:#fff;
}
*{margin:0;padding:0;box-sizing:border-box}
html,body{width:891px;height:1200px;overflow:hidden;background:var(--white)}
body{font-family:"Open Sans",sans-serif;color:var(--ink);position:relative}
.brand{position:absolute;left:45px;top:30px;display:flex;align-items:center;gap:10px}
.brand-mark{width:22px;height:22px;border-radius:50%;background:var(--orange)}
.brand-name{font-size:26px;font-weight:600;color:var(--orange);line-height:1}
.search{position:absolute;left:765px;top:32px;width:105px;height:22px;border:1px solid var(--line);font-size:10px;color:#aaa;padding:4px 8px}
.social{position:absolute;left:768px;top:62px;display:flex;gap:6px}
.social span{width:16px;height:16px;border:1px solid #bbb;border-radius:50%}
.nav{position:absolute;left:0;top:100px;width:891px;height:30px;border-bottom:1px solid var(--line);display:flex;padding-left:55px;gap:30px;font-size:10px;font-weight:600}
.nav a{color:#555;text-decoration:none;padding-top:6px;height:30px}
.nav a.active{color:var(--orange);border-bottom:3px solid var(--orange)}
.hero{position:absolute;left:0;top:131px;width:891px;height:290px;background:linear-gradient(#f8f8f8,var(--hero))}
.hero-photo{position:absolute;left:40px;top:30px;width:260px;height:190px;border:8px solid var(--white);background:linear-gradient(135deg,#d9dde2,#8a9099);box-shadow:0 3px 8px rgba(0,0,0,.2)}
.hero-title{position:absolute;left:490px;top:52px;font-size:28px;font-weight:700;color:#444;white-space:nowrap}
.hero-list{position:absolute;left:490px;top:108px;list-style:none}
.hero-list li{display:flex;align-items:center;gap:14px;height:45px;color:var(--orange);font-size:16px;font-weight:600}
.plus{width:28px;height:28px;border-radius:50%;background:var(--orange);color:var(--white);font-size:22px;font-weight:700;display:flex;align-items:center;justify-content:center;line-height:1}
.perks{position:absolute;left:0;top:430px;width:891px;height:175px}
.perks-rule{position:absolute;left:40px;right:40px;top:30px;border-top:1px solid var(--line)}
.perk{position:absolute;top:8px;width:230px}
.perk-icon{width:44px;height:44px;border-radius:50%;border:1px solid #ccc;background:var(--white);margin-bottom:14px}
.perk h3{font-size:13px;font-weight:700;color:#444;margin-bottom:6px}
.perk p{font-size:10px;line-height:15px;color:var(--muted)}
.features{position:absolute;left:0;top:730px;width:891px;height:470px;background:var(--band)}
.features h2{position:absolute;left:55px;top:62px;font-size:17px;font-weight:600;color:#444}
.feature-list{position:absolute;left:55px;top:108px;list-style:none}
.feature-list li{display:flex;align-items:center;gap:14px;height:30px;font-size:11px;color:#555}
.feature-list li::before{content:"";width:18px;height:18px;border-radius:50%;border:2px solid #999;background:var(--white)}
.feature-list li.current{color:var(--orange)}
.feature-list li.current::before{border-color:var(--orange)}
.phones{position:absolute;left:500px;top:40px;width:280px;height:430px;border-radius:30px 30px 0 0;background:linear-gradient(160deg,#f5f5f5,#bfc3c8)}
</style>
</head>
<body>
<header>
  <div class="brand"><span class="brand-mark"></span><span class="brand-name">Payvinta</span></div>
  <div class="search">Search...</div>
  <div class="social"><span></span><span></span><span></span><span></span><span></span></div>
  <nav class="nav">
    <a class="active">HOME ⌄</a><a>SHOP ⌄</a><a>PARAMETER ⌄</a><a>REGISTER ⌄</a><a>PLANS ⌄</a><a>CONTACT</a>
  </nav>
</header>

<section class="hero">
  <div class="hero-photo" role="img" aria-label="Tablet showing hands typing on a keyboard"></div>
  <h1 class="hero-title">WITH PAYVINTA YOU CAN:</h1>
  <ul class="hero-list">
    <li><span class="plus">+</span>SHOP ANYWHERE</li>
    <li><span class="plus">+</span>DOWNLOAD PREMIUM FILES</li>
    <li><span class="plus">+</span>BOOK TICKETS</li>
  </ul>
</section>

<section class="perks">
  <div class="perks-rule"></div>
  <div class="perk" style="left:85px"><div class="perk-icon"></div><h3>INSTANT TRANSACTIONS</h3><p>Move funds between accounts in seconds with instant confirmation, clear receipts and no waiting for bank processing or manual checks.</p></div>
  <div class="perk" style="left:330px"><div class="perk-icon"></div><h3>SAFE ONLINE ENVIRONMENT</h3><p>Every payment is protected by layered encryption, device checks and real-time monitoring so your balance stays private and secure.</p></div>
  <div class="perk" style="left:620px"><div class="perk-icon"></div><h3>GREAT CUSTOMER SUPPORT</h3><p>Our friendly support team answers questions around the clock by chat and email, helping you solve issues quickly and easily.</p></div>
</section>

<section class="features">
  <h2>FEATURES OF OUR PAYVINTA SYSTEM</h2>
  <ul class="feature-list">
    <li>Send and receive money with any verified user.</li>
    <li>Fund your wallet by card or bank transfer.</li>
    <li>Withdraw balance to your local bank account.</li>
    <li class="current">Pay online stores with a single secure click.</li>
    <li>Track every transaction in a detailed history.</li>
    <li>Set spending limits and instant payment alerts.</li>
    <li>Hold balances in multiple major currencies.</li>
    <li>Create invoices and request payments from clients.</li>
    <li>Enable two-step login for extra protection.</li>
    <li>Export monthly statements in a printable format.</li>
  </ul>
  <div class="phones" role="img" aria-label="Two smartphones showing the wallet app screens"></div>
</section>
</body>
</html>
```